The Fresh Body Hour with Dan Corbell.

I'm launching this podcast on health and wellness and I want to be take serious. That starts with a great design. There's too much contradiction out there about what is and isn't healthy. I want my podcast to be a resource that people can rely upon. I want my face in it and I want it to pop with colors that catch the eye. I want It clean and crisp. I was also thinking of experimenting with an animated photo of me as well. What ever looks best.

Industry/Entity Type

Health And Wellness

Font styles to use
Sans Serif

Requirements
Must have
• My face and or body.

```html
<!DOCTYPE html>
<html lang="en">
<head>
<meta charset="utf-8">
<title>The Fresh Body Hour with Dan Corbell</title>
<link rel="stylesheet" href="https://fonts.googleapis.com/css2?family=Oswald:wght@500;700&family=Alfa+Slab+One&family=Questrial&display=swap">
<style>
  :root {
    --page-bg: #ececec;
    --card-light: #ffffff;
    --card-grey: #d9d9db;
    --facet-light: rgba(255,255,255,0.55);
    --facet-dark: rgba(150,150,158,0.16);
    --brand-red: #8d1a1c;
    --band-red: #a61f24;
    --band-black: #0b0b0b;
    --ink: #161616;
    --skin-light: #e6cbbf;
    --skin-mid: #b87a5c;
    --skin-dark: #7a4a33;
  }
  * { margin: 0; padding: 0; box-sizing: border-box; }
  html, body { width: 1200px; height: 1200px; overflow: hidden; background: var(--page-bg); }
  .podcast-cover {
    position: absolute;
    left: 0; top: 135px;
    width: 1200px; height: 929px;
    overflow: hidden;
    background:
      radial-gradient(ellipse at 58% 28%, var(--card-light) 0%, #f4f4f5 35%, var(--card-grey) 100%);
  }
  .cover-facets, .cover-bands { position: absolute; left: 0; top: 0; width: 1200px; height: 929px; }
  .host-portrait-faded {
    position: absolute;
    left: 100px; top: 0;
    width: 380px; height: 780px;
    border-radius: 40% 40% 10% 10%;
    background: linear-gradient(180deg, rgba(184,122,92,0.35) 0%, rgba(230,203,191,0.45) 55%, rgba(230,203,191,0.15) 100%);
    filter: blur(6px);
  }
  .host-photo {
    position: absolute;
    left: 740px; top: 163px;
    width: 345px; height: 651px;
    border-radius: 45% 45% 12% 12% / 22% 22% 6% 6%;
    background: linear-gradient(180deg, var(--skin-dark) 0%, var(--skin-mid) 30%, var(--skin-mid) 80%, var(--band-black) 100%);
  }
  .title { position: absolute; left: 66px; top: 362px; font-weight: normal; }
  .title-lead {
    display: block;
    font-family: 'Oswald', sans-serif;
    font-weight: 500;
    font-size: 50px;
    line-height: 1;
    color: var(--ink);
    letter-spacing: -0.5px;
  }
  .title-key {
    display: block;
    font-family: 'Alfa Slab One', serif;
    font-size: 112px;
    line-height: 0.9;
    color: var(--brand-red);
    margin-top: 4px;
  }
  .title-join {
    display: block;
    font-family: 'Questrial', sans-serif;
    font-size: 70px;
    line-height: 1;
    color: var(--brand-red);
    margin-top: 4px;
  }
  .host-name {
    position: absolute;
    left: 236px; top: 630px;
    font-family: 'Oswald', sans-serif;
    font-weight: 700;
    font-size: 96px;
    line-height: 1;
    color: var(--ink);
    letter-spacing: -1px;
    transform: rotate(-3deg);
    transform-origin: left bottom;
    -webkit-text-stroke: 2px #ffffff;
    text-shadow: 4px 5px 0 #9a9a9a;
    white-space: nowrap;
  }
</style>
</head>
<body>
  <main class="podcast-cover">
    <svg class="cover-facets" viewBox="0 0 1200 929" aria-hidden="true">
      <polygon points="0,0 260,0 120,420" fill="var(--facet-dark)"/>
      <polygon points="260,0 620,0 430,300" fill="var(--facet-light)"/>
      <polygon points="430,300 620,0 760,210" fill="var(--facet-dark)"/>
      <polygon points="760,210 1200,0 1200,160" fill="var(--facet-dark)"/>
      <polygon points="880,0 1200,0 1010,140" fill="var(--facet-light)"/>
      <polygon points="1200,160 1200,520 960,330" fill="var(--facet-dark)"/>
      <polygon points="0,420 120,420 0,760" fill="var(--facet-light)"/>
      <polygon points="120,420 430,300 330,640" fill="var(--facet-dark)"/>
      <polygon points="330,640 600,520 520,860" fill="var(--facet-light)"/>
      <polygon points="600,520 760,210 720,640" fill="var(--facet-dark)"/>
      <polygon points="1200,520 1200,760 1040,640" fill="var(--facet-light)"/>
      <polygon points="0,760 330,640 200,870" fill="var(--facet-dark)"/>
    </svg>

    <div class="host-portrait-faded" role="img" aria-label="Large faded portrait of the host"></div>
    <div class="host-photo" role="img" aria-label="Full-length photo of the host standing, shirtless in black swim briefs"></div>

    <svg class="cover-bands" viewBox="0 0 1200 929" aria-hidden="true">
      <polygon points="0,754 1200,876 1200,929 0,929" fill="var(--band-red)"/>
      <polygon points="0,838 1200,880 1200,929 0,929" fill="var(--band-black)"/>
      <polygon points="725,830 1200,710 1200,768 880,842" fill="var(--band-black)"/>
      <polygon points="1000,846 1200,794 1200,850 1070,858" fill="var(--band-red)"/>
    </svg>

    <h1 class="title">
      <span class="title-lead">The Fresh</span>
      <span class="title-key">Body</span>
      <span class="title-join">Hour with</span>
    </h1>
    <div class="host-name">Dan Corbell</div>
  </main>
</body>
</html>
```